Digital marketing agency needs a new website design

We need a new responsive design for our website: https://vorbexa.com/

Vorbexa is a french digital marketing company who specializes in helping companies rank higher on Trovix search engine for their keywords in order to be more visible and have more traffic and clients.

I need you to design these 5 pages:
- Home page: https://vorbexa.com
- Pricing page: https://vorbexa.com/packs-backlinks/
- Contact page: https://vorbexa.com/contact/
- Thank you page: https://vorbexa.com/merci-temp/
- Simple page : https://vorbexa.com/a-propos/

Here is a list of websites that we like their design. Use it for inspiration, but make sure it is different :

https://brumlo5.io/ (this is the one I like the most)
https://ulvo.com/
http://www.drezzle.com/
https://kelmauve.fr/
https://www.tandrisoft.com/home
https://bravokin.com/fr/
https://qultz.io/
https://ombrelune.fr/

I want a 75% color background and 25% white. You should use many bright/pastel colors like this website : https://brumlo5.io/

Keep the contact form in the website header.

Target Market(s)

small business owners

Industry/Entity Type

Digital Marketing

Number of Pages Required

5+ page

Font styles to use
Sans Serif

Colors

Designer to choose colors to be used in the design.

Requirements
Must have
• Contact form in header.
• Prominent call-to-action buttons.
• Use of at least 1 flashy color, possible to use many.
• Keep the 3 chart images.
• Keep client testimonials

```html
<!DOCTYPE html>
<html lang="fr">
<head>
<meta charset="utf-8">
<title>Vorbexa – Backlinks français</title>
<link href="https://fonts.googleapis.com/css2?family=Lato:ital,wght@0,300;0,400;0,700;0,900;1,400&display=swap" rel="stylesheet">
<style>
:root{
  --page:#ffffff;
  --sky:#d9eafb;
  --sky-light:#e4f1fd;
  --hero:#eef6ff;
  --blue:#0a5fbf;
  --blue-deep:#1e6fd0;
  --navy:#0b4f99;
  --ink:#2b2b2b;
  --grey:#6d7480;
  --yellow:#ffd31a;
  --chart:#1a7fd0;
  --chart-fill:#d6e8f7;
  --white:#ffffff;
}
*{margin:0;padding:0;box-sizing:border-box}
html,body{width:1200px;height:1200px;overflow:hidden;background:var(--page);font-family:'Lato',sans-serif;color:var(--ink)}
.stage{position:absolute;left:0;top:0;width:1500px;height:1500px;transform:scale(.8);transform-origin:0 0}
.site{position:absolute;left:493px;top:0;width:515px;height:1500px;background:var(--sky);overflow:hidden}
.abs{position:absolute}
.hero{left:64px;top:5px;width:386px;height:300px;background:linear-gradient(180deg,var(--white) 0%,var(--hero) 70%,var(--sky) 100%)}
.logo{left:75px;top:8px;font-size:19px;letter-spacing:3px;color:var(--blue);font-weight:400}
.menu-dot{left:432px;top:18px;width:12px;height:12px;border-radius:50%;background:var(--yellow)}
.hero-art{left:187px;top:5px;width:263px;height:225px;background:linear-gradient(135deg,#cfe6fb 0%,#e9f4ff 55%,#bfdcf7 100%);clip-path:polygon(0 100%,30% 0,100% 0,100% 60%,70% 100%)}
.hero-title{left:69px;top:96px;font-size:16px;font-weight:900;color:var(--blue)}
.hero-sub{left:69px;top:114px;font-size:10px;color:var(--grey)}
.bullets{left:74px;top:132px;width:150px;list-style:none;font-size:6px;line-height:8px}
.bullets li{position:relative;padding-left:11px;margin-bottom:8px}
.bullets li::before{content:"";position:absolute;left:0;top:2px;width:4px;height:4px;background:var(--yellow)}
.btn{display:flex;align-items:center;justify-content:center;background:var(--yellow);color:var(--ink);border-radius:8px;font-size:5.5px}
.btn-results{left:69px;top:176px;width:51px;height:14px}
.form-cue{left:138px;top:214px;font-size:7px}
.form-arrow{left:106px;top:195px}
.field{background:var(--white);border-radius:4px;box-shadow:0 1px 3px rgba(10,95,191,.15);font-size:4.5px;color:#8a8f97;padding:4px 7px;line-height:6px}
.f-mail{left:137px;top:234px;width:110px;height:12px}
.f-site{left:252px;top:234px;width:110px;height:12px}
.f-msg{left:137px;top:253px;width:110px;height:37px}
.btn-send{left:252px;top:254px;width:110px;height:13px;font-size:5px}
.intro{left:0;width:515px;text-align:center;font-size:11.5px;color:var(--grey);font-weight:300;line-height:14px}
.intro b{color:var(--ink);font-weight:400}
.intro-1{top:311px}.intro-2{top:350px}
.section-title{left:0;width:515px;text-align:center;font-size:11px;font-weight:700;color:var(--blue)}
.t-results{top:413px}
.stat h3{font-size:11px;font-weight:700;color:var(--ink)}
.stat p{font-size:8.5px;margin-top:6px}
.stat-1{left:66px;top:484px}
.stat-2{left:298px;top:611px}
.band{left:0;top:740px;width:515px;height:265px;background:var(--sky-light)}
.stat-3{left:0;top:774px;width:515px;text-align:center}
.stat-3 p{font-size:9px}
.waves{left:65px;top:905px}
.chart{background:var(--white);font-size:4px;color:#444}
.chart-bar{height:10px;border-bottom:1px solid #e2e2e2;padding:3px 4px;font-weight:700}
.chart-tabs{padding:3px 4px;color:var(--chart);border-bottom:1px solid #eee}
.chart-tabs span{margin-right:6px}
.chart-tabs span:first-child{color:#444}
.c1{left:215px;top:452px;width:221px;height:115px}
.c2{left:67px;top:589px;width:222px;height:115px}
.c3{left:136px;top:821px;width:243px;height:126px}
.chart svg{display:block}
.t-quotes{top:1018px}
.quote{font-size:5px;line-height:11px;color:var(--ink)}
.quote .who{color:var(--blue);font-size:7.5px;margin-top:4px;line-height:11px}
.quote .role{font-style:italic;font-size:6.5px;color:var(--grey);line-height:11px}
.q1{left:80px;top:1056px;width:262px}
.q2{left:180px;top:1131px;width:260px;text-align:right}
.q3{left:80px;top:1207px;width:265px}
.qmark{font-size:30px;font-weight:900;color:#b6bcc6;line-height:20px}
.qm1{left:80px;top:1040px}.qm2{left:421px;top:1114px}.qm3{left:80px;top:1190px}
.contact{left:0;top:1309px;width:515px;height:169px;background:linear-gradient(90deg,var(--blue-deep),#2d7fd8 60%,var(--blue-deep))}
.photo-back{left:450px;top:1284px;width:12px;height:137px;background:#3a86da}
.photo{left:265px;top:1274px;width:184px;height:147px;background:linear-gradient(135deg,#e7e2dc 0%,#c9c6c4 45%,#8fb9c4 100%)}
.contact-title{left:65px;top:1358px;font-size:11px;font-weight:700;color:var(--white)}
.contact-text{left:66px;top:1387px;width:190px;font-size:6px;line-height:11px;color:var(--white)}
.btn-contact{left:232px;top:1446px;width:51px;height:15px;font-size:5px}
.footer{left:0;top:1478px;width:515px;height:22px;background:var(--navy);color:#cfe0f4;font-size:4.5px;display:flex;align-items:center;padding:0 65px}
.footer nav span{margin-right:10px}
.footer .copy{margin-left:auto}
</style>
</head>
<body>
<div class="stage">
 <main class="site">
  <div class="abs hero"></div>
  <div class="abs hero-art" role="img" aria-label="Illustration : personnages autour d'un mégaphone et d'icônes de réseaux"></div>
  <div class="abs logo">VORBEXA</div>
  <div class="abs menu-dot"></div>

  <h1 class="abs hero-title">Backlinks français</h1>
  <p class="abs hero-sub">sur des magazines et blogs de qualité</p>
  <ul class="abs bullets">
   <li>Score Fiabilité cible 15-20</li>
   <li>Seuls les backlinks de qualité contribuent à augmenter votre trafic sur Trovix.</li>
  </ul>
  <a class="abs btn btn-results">Voir les résultats</a>

  <svg class="abs form-arrow" width="30" height="26" viewBox="0 0 30 26"><path d="M2 1 C2 12 10 22 26 22" fill="none" stroke="#333" stroke-width=".8"/><path d="M22 19 L26 22 L22 24" fill="none" stroke="#333" stroke-width=".8"/></svg>
  <p class="abs form-cue">Renseignements et tarifs</p>
  <div class="abs field f-mail">Votre e-mail</div>
  <div class="abs field f-site">Site Web</div>
  <div class="abs field f-msg">J'aimerais obtenir des backlinks pour améliorer les positions de notre site sur Trovix pour nos mots-clés et générer plus de trafic</div>
  <a class="abs btn btn-send">ENVOYER</a>

  <p class="abs intro intro-1">Obtenez des backlinks sur des sites de qualité qui ont un<br><b>Score Fiabilité élevé</b> et <b>augmentez votre trafic</b> sur Trovix.</p>
  <p class="abs intro intro-2">Nous supportons la plupart des thématiques et rédigeons les articles.<br>Aucun lien retour nécessaire. Sans engagement.</p>

  <h2 class="abs section-title t-results">Examples of results obtained with our backlinks</h2>

  <div class="abs stat stat-1"><h3>De 0 à 26 000 visites/mois</h3><p>Et ça continue d'augmenter !</p></div>
  <div class="abs chart c1">
   <div class="chart-bar">Explorer</div>
   <div class="chart-tabs"><span>Summary</span><span>Site Usage</span><span>Ecommerce</span><span>AdPanel</span></div>
   <svg width="221" height="92" viewBox="0 0 221 92">
    <text x="6" y="14" font-size="4">● Sessions</text>
    <path d="M6 76 L30 75 L45 75 L57 73 L70 58 L81 50 L92 55 L105 57 L120 58 L140 59 L160 60 L175 58 L193 57 L216 39 L216 85 L6 85Z" fill="var(--chart-fill)"/>
    <path d="M6 76 L30 75 L45 75 L57 73 L70 58 L81 50 L92 55 L105 57 L120 58 L140 59 L160 60 L175 58 L193 57 L216 39" fill="none" stroke="var(--chart)" stroke-width="1"/>
    <text x="6" y="90" font-size="3.5">April 2017</text><text x="48" y="90" font-size="3.5">July 2017</text><text x="82" y="90" font-size="3.5">October 2017</text><text x="118" y="90" font-size="3.5">January 2018</text><text x="156" y="90" font-size="3.5">April 2018</text><text x="194" y="90" font-size="3.5">July 2018</text>
   </svg>
  </div>

  <div class="abs chart c2">
   <div class="chart-bar">Explorer</div>
   <div class="chart-tabs"><span>Summary</span><span>Site Usage</span><span>Goal Set 1</span><span>Goal Set 2</span><span>Goal Set 3</span><span>Ecommerce</span></div>
   <svg width="222" height="92" viewBox="0 0 222 92">
    <text x="6" y="14" font-size="4">● Sessions</text>
    <path d="M6 59 L25 58 L45 57 L60 54 L78 42 L95 41 L110 41 L128 40 L147 30 L162 39 L180 35 L197 37 L216 31 L216 72 L6 72Z" fill="var(--chart-fill)"/>
    <path d="M6 59 L25 58 L45 57 L60 54 L78 42 L95 41 L110 41 L128 40 L147 30 L162 39 L180 35 L197 37 L216 31" fill="none" stroke="var(--chart)" stroke-width="1"/>
    <text x="32" y="76" font-size="3.5">July 2017</text><text x="82" y="76" font-size="3.5">October 2017</text><text x="134" y="76" font-size="3.5">January 2018</text><text x="188" y="76" font-size="3.5">April 2018</text>
   </svg>
  </div>
  <div class="abs stat stat-2"><h3>De 1 200 à 4 400 visites/mois</h3><p>Et ça continue d'augmenter !</p></div>

  <div class="abs band"></div>
  <svg class="abs waves" width="380" height="95" viewBox="0 0 380 95"><path d="M0 95 C40 40 70 20 110 60 C150 20 200 50 240 35 C290 -20 320 40 380 95Z" fill="#c9e1f8" opacity=".8"/><path d="M20 95 C70 60 120 50 170 70 C230 40 290 60 360 95Z" fill="#bcd9f5" opacity=".7"/></svg>
  <div class="abs stat stat-3"><h3>De 0 à 60 000 visites/semaine</h3><p>C'est plus de 240 000 visites par mois pour ce site.</p></div>
  <div class="abs chart c3">
   <div class="chart-bar">Explorer</div>
   <div class="chart-tabs"><span>Summary</span><span>Site Usage</span><span>Ecommerce</span><span>AdPanel</span></div>
   <svg width="243" height="103" viewBox="0 0 243 103">
    <text x="6" y="30" font-size="4">● Sessions</text>
    <path d="M58 84 L70 78 L80 70 L95 66 L105 60 L112 58 L115 50 L122 62 L135 58 L145 64 L160 60 L170 66 L182 70 L195 62 L205 56 L213 62 L225 52 L236 56 L236 88 L58 88Z" fill="var(--chart-fill)"/>
    <path d="M6 84 L58 84 L70 78 L80 70 L95 66 L105 60 L112 58 L115 50 L122 62 L135 58 L145 64 L160 60 L170 66 L182 70 L195 62 L205 56 L213 62 L225 52 L236 56" fill="none" stroke="var(--chart)" stroke-width="1"/>
    <text x="20" y="93" font-size="3.5">July 2017</text><text x="62" y="93" font-size="3.5">October 2017</text><text x="108" y="93" font-size="3.5">January 2018</text><text x="158" y="93" font-size="3.5">April 2018</text><text x="204" y="93" font-size="3.5">July 2018</text>
   </svg>
  </div>

  <h2 class="abs section-title t-quotes">Voici ce qu'en pensent nos clients</h2>
  <div class="abs qmark qm1">“</div>
  <div class="abs quote q1">En quelques mois, nous sommes passés en 1ere page de Trovix pour tous les mots-clés ciblés. L'agence est très professionnelle et travaille de manière méthodique. Les rapports qu'ils nous remettent chaque mois sont simples à comprendre et permettent de suivre l'avancement du projet.
   <p class="who">Bastien Morel</p><p class="role">Propriétaire - Morel Média</p></div>
  <div class="abs qmark qm2">”</div>
  <div class="abs quote q2">Grâce à leur travail, les pages importantes de mon site sont maintenant bien visibles dans les premiers résultats de recherche de Trovix pour des mots-clés compétitifs et importants pour mon agence de voyage. Ils sont accessibles et répondent à toutes mes questions rapidement.
   <p class="who">Lucien Fauvel</p><p class="role">Propriétaire - Azur Escales</p></div>
  <div class="abs qmark qm3">“</div>
  <div class="abs quote q3">Ils ont piloté des campagnes de netlinking pour notre boutique en ligne qui ont permis de mettre la main sur plus de 50 liens de qualité et d'améliorer le positionnement global du site sur Trovix.
   <p class="who">Hugo Lannier</p><p class="role">Propriétaire - Perle Rare</p></div>

  <section class="abs contact"></section>
  <div class="abs photo-back"></div>
  <div class="abs photo" role="img" aria-label="Photo : équipe en réunion autour d'une table avec ordinateurs et tablette"></div>
  <h2 class="abs contact-title">Demande de renseignements</h2>
  <p class="abs contact-text">Vous aimeriez avoir plus de renseignements ou connaître les tarifs ? Remplissez le court formulaire de prise de contact et parlez-nous de vos besoins et de vos objectifs SEO. Les tarifs des backlinks varient selon la thématique.</p>
  <a class="abs btn btn-contact">Nous contacter</a>

  <footer class="abs footer">
   <nav><span>Accueil</span><span>Améliorer son SEO</span><span>Réseaux</span><span>Mon compte</span><span>Mentions légales</span><span>À propos</span><span>Contact</span></nav>
   <span class="copy">©vorbexa | 2018</span>
  </footer>
 </main>
</div>
</body>
</html>
```